An insurance broker wants to represent the company's vision visually and textually.

My company, with a total of 10 employees, developed a vision this year. Now, we want to display this vision in the form of a two-meter-high visual that will be mounted on the wall. This ensures that the vision is always visible to our employees, as well as to our clients and partners when they visit our office.

Here's my idea: the vision will be accompanied by a fitting image, with the text of the vision itself elegantly written in a beautiful font. Our vision reads: "Every company always has a perfectly tailored future solution for greater financial security, freedom, and joy."

A bit about my company: we are an insurance broker, and our services are primarily designed for corporate clients.

```html
<!DOCTYPE html>
<html lang="en">
<head>
<meta charset="utf-8">
<title>Our Vision</title>
<link rel="stylesheet" href="https://fonts.googleapis.com/css2?family=Playfair+Display:wght@900&family=Kaushan+Script&family=League+Spartan:wght@800&display=swap">
<style>
  :root {
    --forest: #02342e;
    --coral: #f0645a;
    --gold: #e7a733;
    --white: #fbfcfd;
  }
  html, body {
    margin: 0;
    padding: 0;
    width: 1200px;
    height: 1200px;
    overflow: hidden;
    background: var(--forest);
  }
  .vision-poster {
    position: relative;
    width: 1200px;
    height: 1200px;
    background: var(--forest);
  }
  .puzzle-artwork {
    position: absolute;
    left: 328px;
    top: 56px;
    width: 547px;
    height: 326px;
    clip-path: polygon(35% 0, 65% 0, 65% 30%, 100% 30%, 100% 100%, 0 100%, 0 30%, 35% 30%);
    background: linear-gradient(160deg, var(--coral) 0%, var(--gold) 55%, var(--coral) 100%);
  }
  .frame-corners {
    position: absolute;
    inset: 0;
    width: 1200px;
    height: 1200px;
  }
  .frame-corners path {
    fill: none;
    stroke: var(--white);
    stroke-width: 11;
  }
  .line {
    position: absolute;
    left: 0;
    width: 1200px;
    text-align: center;
    line-height: 1;
    white-space: nowrap;
    margin: 0;
  }
  .serif-caps {
    font-family: "Playfair Display", Georgia, serif;
    font-weight: 900;
    text-transform: uppercase;
  }
  .headline-coral {
    top: 425px;
    font-size: 92px;
    letter-spacing: 4px;
    color: var(--coral);
  }
  .script-link {
    font-family: "Kaushan Script", cursive;
    font-size: 52px;
    color: var(--gold);
  }
  .link-always { top: 524px; }
  .link-greater { top: 766px; }
  .headline-white {
    color: var(--white);
  }
  .line-tailored {
    top: 603px;
    font-size: 81px;
    letter-spacing: 3px;
  }
  .line-solution {
    top: 693px;
    font-size: 70px;
    letter-spacing: 3px;
  }
  .sans-caps {
    font-family: "League Spartan", "Arial Black", sans-serif;
    font-weight: 800;
    text-transform: uppercase;
    font-size: 88px;
    color: var(--white);
    letter-spacing: 0;
  }
  .line-financial { top: 860px; }
  .line-security { top: 956px; }
  .line-joy { top: 1052px; }
</style>
</head>
<body>
<main class="vision-poster">
  <div class="puzzle-artwork" role="img" aria-label="Pyramid of interlocking puzzle pieces in coral, gold and white"></div>

  <svg class="frame-corners" viewBox="0 0 1200 1200" aria-hidden="true">
    <path d="M116.5 463 V393.5 H189"/>
    <path d="M1011 393.5 H1083.5 V463"/>
    <path d="M116.5 1072 V1141.5 H189"/>
    <path d="M1011 1141.5 H1083.5 V1072"/>
  </svg>

  <h1 class="line serif-caps headline-coral">Every Company</h1>
  <p class="line script-link link-always">always has a</p>
  <p class="line serif-caps headline-white line-tailored">Perfectly Tailored</p>
  <p class="line serif-caps headline-white line-solution">Future Solution</p>
  <p class="line script-link link-greater">for greater</p>
  <p class="line sans-caps line-financial">Financial</p>
  <p class="line sans-caps line-security">Security, Freedom</p>
  <p class="line sans-caps line-joy">and Joy.</p>
</main>
</body>
</html>
```